Business Card Design Project

We need a logo design for a new company based in Southern California called "Norvale Security Services, Inc." We install security and camera systems for homeowners and business, to protect their assets.
Updates

Project Deadline Extended
Reason: LOGO Design completes in eight days. Would like that design decided before we finish the business cards. Thanks...

Target Market(s)

Homeowners and business owners looking for additional protection of their assets.

Industry/Entity Type

Security

Font styles to use
Serif

Requirements
Must have
• Company Name
Office# 909-472-3615
Service# 909-472-3616
email: NorvaleSecurity@brimwell.net
address: 48620 Thorncrest Lane Rancho Cucamonga, CA 91704
Nice to have
• Serving Southern California

```html
<!DOCTYPE html>
<html lang="en">
<head>
<meta charset="utf-8">
<title>Norvale Security Services – Business Card</title>
<link href="https://fonts.googleapis.com/css2?family=Michroma&display=swap" rel="stylesheet">
<style>
  :root {
    --page-bg: #e9ecef;
    --card-white: #ffffff;
    --brand-blue: #1b8fd2;
    --band-blue-light: #1aa3e0;
    --band-blue-dark: #1a78b8;
    --navy: #23406f;
    --text-light: #ffffff;
  }
  html, body {
    margin: 0;
    width: 1200px;
    height: 900px;
    overflow: hidden;
    background: var(--page-bg);
  }
  .card-stage {
    width: 1200px;
    height: 900px;
    display: flex;
    align-items: center;
    justify-content: center;
  }
  .business-card {
    width: 900px;
    height: 520px;
    filter: drop-shadow(0 10px 24px rgba(0,0,0,0.18));
  }
  .card-text { font-family: "Michroma", sans-serif; }
  .brand-name { fill: var(--brand-blue); font-size: 54px; letter-spacing: 1px; }
  .brand-sub { fill: var(--brand-blue); font-size: 21px; letter-spacing: 1.5px; }
  .person-name { fill: var(--text-light); font-size: 17px; letter-spacing: 1.5px; }
  .person-role, .office-address { fill: var(--text-light); font-size: 13.5px; letter-spacing: 0.8px; }
  .contact-line { fill: var(--text-light); font-size: 13.5px; letter-spacing: 0.6px; }
  .divider { stroke: var(--text-light); stroke-width: 1.2; opacity: 0.85; }
  .contact-icon { fill: var(--text-light); }
  .icon-glyph { fill: var(--band-blue-dark); }
</style>
</head>
<body>
<main class="card-stage">
  <svg class="business-card" viewBox="0 0 900 520" xmlns="http://www.w3.org/2000/svg" aria-label="Norvale Security Services business card">
    <defs>
      <clipPath id="card-shape">
        <path d="M0,170 Q0,130 40,130 L170,130 Q205,130 210,95 L214,45 Q218,0 262,0 L855,0 Q900,0 900,45 L900,475 Q900,520 855,520 L45,520 Q0,520 0,475 Z"/>
      </clipPath>
      <linearGradient id="band-gradient" x1="0" y1="1" x2="1" y2="0">
        <stop offset="0" stop-color="var(--band-blue-dark)"/>
        <stop offset="1" stop-color="var(--band-blue-light)"/>
      </linearGradient>
    </defs>

    <g clip-path="url(#card-shape)">
      <rect class="card-base" width="900" height="520" fill="var(--card-white)"/>
      <path class="navy-swoosh" d="M0,300 C250,336 560,226 900,146 L900,176 C560,256 260,366 0,336 Z" fill="var(--navy)"/>
      <path class="blue-band" d="M0,338 C260,368 560,258 900,178 L900,520 L0,520 Z" fill="url(#band-gradient)"/>
    </g>

    <g class="brand-block card-text">
      <text class="brand-name" x="34" y="226">NORVALE</text>
      <text class="brand-sub" x="36" y="260">SECURITY SERVICES</text>
    </g>

    <g class="identity-block card-text" text-anchor="end">
      <text class="person-name" x="470" y="350">DANIEL REYES</text>
      <text class="person-role" x="470" y="376">Owner / C.E.O</text>
      <text class="office-address" x="470" y="426">48620 Thorncrest Lane,</text>
      <text class="office-address" x="470" y="450">Rancho Cucamonga, CA 91704</text>
    </g>

    <line class="divider" x1="490" y1="300" x2="490" y2="470"/>

    <g class="contact-block card-text">
      <circle class="contact-icon" cx="514" cy="318" r="8"/>
      <path class="icon-glyph" d="M510,314 q1,-2 3,-1 l1,2 -1,1 q1,3 4,4 l1,-1 2,1 q1,2 -1,3 q-7,-1 -9,-9z"/>
      <text class="contact-line" x="530" y="323">909-472-3615</text>

      <circle class="contact-icon" cx="514" cy="344" r="8"/>
      <rect class="icon-glyph" x="511" y="339" width="6" height="10" rx="1"/>
      <text class="contact-line" x="530" y="349">909-472-3616</text>

      <circle class="contact-icon" cx="514" cy="370" r="8"/>
      <rect class="icon-glyph" x="509" y="366" width="10" height="7" rx="1"/>
      <text class="contact-line" x="530" y="375">909-472-3617</text>

      <circle class="contact-icon" cx="514" cy="410" r="8"/>
      <path class="icon-glyph" d="M509,407 h10 v7 h-10z M509,407 l5,4 5,-4" stroke="var(--band-blue-dark)" stroke-width="0.5"/>
      <text class="contact-line" x="530" y="415">NorvaleSecurity@brimwell.net</text>

      <circle class="contact-icon" cx="514" cy="436" r="8"/>
      <circle class="icon-glyph" cx="514" cy="436" r="5"/>
      <line x1="509" y1="436" x2="519" y2="436" stroke="var(--text-light)" stroke-width="1"/>
      <text class="contact-line" x="530" y="441">www.norvalesecurity.com</text>
    </g>
  </svg>
</main>
</body>
</html>
```